Stationery Design Project

We are a packaging machinery manufacturer that mainly serve the food industry.
We now require a full set of stationary including name card, envelop, letter paper, and etc. to match our company image. The logo has been awarded in a previous contest which is attached here.
Updates
Project Deadline Extended
Reason: We have extended the deadline. We have adjusted the deadline before launch to avoid confusion but it turns out the new date wasn't implemented by the system. All designers please feel free to submit your design. Thank you!
Target Market(s)
B2B customer, including decision maker in food factories, chemical factories, etc.
Industry/Entity Type
Industry
Colors
Designer to choose colors to be used in the design.
Look and feel
Each slider illustrates characteristics of the customer's brand and the style your logo design should communicate.

```html
<!DOCTYPE html>
<html lang="en">
<head>
<meta charset="utf-8">
<title>Takro Presentation Folder</title>
<link rel="stylesheet" href="https://fonts.googleapis.com/css2?family=Open+Sans:wght@400;600;700&display=swap">
<style>
  :root {
    --canvas: #e4e4e4;
    --brand-green: #006837;
    --steel-grey: #8a9096;
    --paper-white: #ffffff;
    --text-grey: #6b6f73;
  }
  * { box-sizing: border-box; margin: 0; padding: 0; }
  html, body {
    width: 1200px;
    height: 900px;
    overflow: hidden;
    background: var(--canvas);
    font-family: "Open Sans", Arial, sans-serif;
  }
  .folder-spread {
    position: relative;
    width: 1200px;
    height: 900px;
  }
  .folder-panel {
    position: absolute;
    top: 140px;
    width: 440px;
    height: 620px;
    overflow: hidden;
  }
  .front-cover { left: 130px; background: var(--steel-grey); }
  .back-cover { left: 630px; background: var(--brand-green); }
  .panel-art { position: absolute; inset: 0; width: 100%; height: 100%; }

  .brand-lockup {
    position: absolute;
    left: 96px;
    top: 282px;
    display: flex;
    align-items: center;
    gap: 10px;
    color: var(--paper-white);
  }
  .brand-square {
    width: 30px;
    height: 30px;
    background: var(--paper-white);
  }
  .brand-name {
    font-weight: 700;
    font-size: 44px;
    line-height: 1;
    letter-spacing: 2px;
  }

  .web-address {
    position: absolute;
    top: 276px;
    left: 0;
    width: 100%;
    text-align: center;
    color: var(--paper-white);
    font-weight: 600;
    font-size: 16px;
  }
  .contact-block {
    position: absolute;
    left: 24px;
    top: 524px;
    color: var(--text-grey);
    font-size: 10px;
    line-height: 13px;
  }
  .contact-lines { display: flex; gap: 8px; margin-top: 6px; }
  .contact-item { display: flex; align-items: center; gap: 3px; }
  .contact-item svg { width: 11px; height: 11px; }
</style>
</head>
<body>
<main class="folder-spread">
  <section class="folder-panel front-cover">
    <svg class="panel-art" viewBox="0 0 440 620" aria-hidden="true">
      <polygon points="400,0 440,0 440,620 128,310" fill="var(--brand-green)"/>
    </svg>
    <div class="brand-lockup">
      <span class="brand-square"></span>
      <span class="brand-name">TAKRO</span>
    </div>
  </section>

  <section class="folder-panel back-cover">
    <p class="web-address">www.takro.com</p>
    <svg class="panel-art" viewBox="0 0 440 620" aria-hidden="true">
      <rect x="410" y="513" width="30" height="62" fill="var(--steel-grey)"/>
      <polygon points="0,515 424,508 392,546 424,584 0,584" fill="var(--paper-white)"/>
    </svg>
    <div class="contact-block">
      <p>Your Office, Building, City</p>
      <p>State XXXXX Country</p>
      <div class="contact-lines">
        <span class="contact-item">
          <svg viewBox="0 0 12 12"><rect x="0.5" y="0.5" width="11" height="11" fill="none" stroke="var(--brand-green)"/><rect x="2.5" y="2" width="3" height="8" fill="var(--brand-green)"/><rect x="7" y="3" width="3" height="2" fill="var(--brand-green)"/><rect x="7" y="6.5" width="3" height="2" fill="var(--brand-green)"/></svg>
          123 456 7890
        </span>
        <span class="contact-item">
          <svg viewBox="0 0 12 12"><path d="M3 1h5v4H3z M1 6h10v5H1z" fill="none" stroke="var(--brand-green)" stroke-width="1.2"/></svg>
          123 456 7890
        </span>
      </div>
    </div>
  </section>
</main>
</body>
</html>
```